Ledgers On Track Business Card Design

We are a bookkeeping and accounting practice and are particularly passionate about Talvo as 'state of the art' accounting software. We offer a number of services which are listed on the back of the card. The logos for LOT have already been developed. There are also other logos of organisations we are involved with - Talvo (both certified advisor and silver partner), GFR, and filerite hub. Regarding colours, we would like to use the colours similar to our website, www.ledgersontrack.com, and these connect with the www.talvo.com.au website. The proposed layout as it is just does not look too great - it looks like an amateur has done it - which is true!

Industry/Entity Type

Accounting

Contact Information for Business Card

The details to appear on the card are found on the files uploaded. I have front and back rough layouts.

```html
<!DOCTYPE html>
<html lang="en">
<head>
<meta charset="utf-8">
<title>Ledgers On Track – Business Card</title>
<link rel="stylesheet" href="https://fonts.googleapis.com/css2?family=Arimo:wght@400&family=Fira+Sans:wght@700&family=Permanent+Marker&display=swap">
<style>
  :root {
    --paper: #ffffff;
    --ink-name: #111111;
    --blue-soft: #5b7fd8;
    --panel: #6889dc;
    --panel-text: #ffffff;
    --brand-blue: #3656d4;
    --brand-green: #4fd40c;
    --abn: #a9b48f;
    --badge-aqua: #1fe9c9;
    --badge-teal: #14a6a2;
    --badge-orange: #e5652a;
    --guild-green: #2b5a3a;
  }
  * { margin: 0; padding: 0; box-sizing: border-box; }
  html, body { width: 1200px; height: 741px; overflow: hidden; background: var(--paper); }
  .card {
    position: relative;
    width: 1200px;
    height: 741px;
    background: var(--paper);
    font-family: "Arimo", Arial, sans-serif;
  }
  .holder {
    position: absolute;
    left: 517px;
    right: 0;
    top: 40px;
    text-align: center;
  }
  .holder-name {
    font-family: "Permanent Marker", Impact, sans-serif;
    font-weight: 400;
    font-size: 58px;
    line-height: 64px;
    color: var(--ink-name);
    letter-spacing: 2px;
    text-transform: uppercase;
  }
  .holder-credentials {
    margin-top: 16px;
    font-size: 35px;
    line-height: 50px;
    color: var(--blue-soft);
    word-spacing: 6px;
  }
  .contact-panel {
    position: absolute;
    left: 517px;
    top: 249px;
    width: 683px;
    height: 303px;
    background: var(--panel);
    color: var(--panel-text);
    font-style: normal;
    padding: 30px 0 0 31px;
    font-size: 33px;
    line-height: 48.5px;
    word-spacing: 4px;
  }
  .brand-dot {
    position: absolute;
    left: 40px;
    top: 282px;
    width: 126px;
    height: 126px;
    border-radius: 50%;
    background: var(--brand-green);
  }
  .brand-name {
    position: absolute;
    left: 216px;
    top: 282px;
    font-family: "Fira Sans", Arial, sans-serif;
    font-weight: 700;
    font-size: 62px;
    line-height: 74px;
    color: var(--brand-blue);
  }
  .brand-abn {
    position: absolute;
    left: 78px;
    top: 428px;
    font-size: 31px;
    line-height: 36px;
    color: var(--abn);
    letter-spacing: 1px;
  }
  .affiliations {
    position: absolute;
    left: 519px;
    top: 592px;
    display: flex;
    align-items: center;
  }
  .affiliations svg { display: block; }
  .guild-name {
    margin-left: 14px;
    color: var(--guild-green);
    font-size: 25px;
    line-height: 30px;
    text-transform: uppercase;
  }
</style>
</head>
<body>
  <main class="card">
    <header class="holder">
      <h1 class="holder-name">Glen Harlow</h1>
      <p class="holder-credentials">B.Com, M.A. Ph D, AGFR<br>Registered BAS Agent</p>
    </header>

    <span class="brand-dot" aria-hidden="true"></span>
    <p class="brand-name">Ledgers<br>On Track</p>
    <p class="brand-abn">ABN 12 345 678 901</p>

    <address class="contact-panel">
      18 Calder Ridge Road,<br>
      Eltham Park&nbsp; VIC&nbsp; 3095<br>
      T&nbsp; 03&nbsp; 9555&nbsp; 0142&nbsp; M&nbsp; 0400555&nbsp; 318<br>
      glen@ledgersontrack.com<br>
      www.ledgersontrack.com
    </address>

    <footer class="affiliations">
      <svg width="320" height="110" viewBox="0 0 320 110" role="img" aria-label="Talvo certified advisor and GFR membership badges">
        <circle cx="54" cy="55" r="54" fill="var(--badge-aqua)"/>
        <circle cx="167" cy="55" r="54" fill="var(--badge-teal)"/>
        <circle cx="276" cy="55" r="39" fill="#ffffff" stroke="var(--badge-orange)" stroke-width="4"/>
      </svg>
      <p class="guild-name">Guild of Financial<br>Registrants</p>
    </footer>
  </main>
</body>
</html>
```